Create the following for my cosmetic business : Logo and packaging design*

Valiremo Beauty is a cosmetic brand of skincare and makeup. I need:

(1) A logo: That represents creativity, beautiful, powerful and royalty. The logo should be unique and fun at sane time. It should be attractive enough for customers to want to identify with it. target audience is anyone who values beauty. The logo should be designed in a way that it will be visibly printable on different surfaces and sizes of different products

(2). Packaging designs: Unique layout of logo and brand on packages (external packages and designs on the body of the products itself) for skincare products (such as body creams, scrubs, bath soap, facial masks, etc). and make up products such as lipsticks, lip gloss, eyeshadow pallettes, contour, eyelashes etc.

Target Market(s)

Skincare products and cosmetics for:

Age: 16 -45
mid-income earners
Vegan friendly

Industry/Entity Type

Cosmetics

Font styles to use
Sans Serif
Script

Requirements
Must have
• include "animals cruelty-free" symbol in one corner somewhere win the design

very creative designs
Nice to have
• Design variations of
1. Dark Background
2. Light background

so I can compare

```html
<!DOCTYPE html>
<html lang="en">
<head>
<meta charset="utf-8">
<title>Valiremo Beauty – Body Cream Packaging</title>
<link rel="stylesheet" href="https://fonts.googleapis.com/css2?family=Jost:wght@400;600&family=Montserrat:wght@600&display=swap">
<style>
  :root{
    --backdrop:#c5dfeb;
    --pink:#e0588f;
    --teal:#36b6c9;
    --sky:#a9d4ec;
    --label:#ffffff;
    --frame:#8a8a8a;
    --ink:#1e1e1e;
    --ink-soft:#555555;
  }
  *{margin:0;padding:0;box-sizing:border-box}
  html,body{width:1200px;height:1200px;overflow:hidden;background:var(--backdrop)}
  .canvas{position:relative;width:1200px;height:1200px}

  .pattern{
    position:absolute;inset:0;
    background:
      radial-gradient(circle at 25% 20%, var(--pink) 0 18%, transparent 19%),
      radial-gradient(circle at 80% 35%, var(--sky) 0 22%, transparent 23%),
      radial-gradient(circle at 20% 75%, var(--sky) 0 20%, transparent 21%),
      radial-gradient(circle at 75% 80%, var(--pink) 0 24%, transparent 25%),
      linear-gradient(135deg, var(--teal), var(--pink) 55%, var(--teal));
  }

  .tube-face{position:absolute;left:130px;top:150px;width:380px;height:860px;overflow:hidden}
  .jar-wrap{position:absolute;left:580px;top:500px;width:560px;height:300px;overflow:hidden}

  .label{
    position:absolute;background:var(--label);
    border-radius:26px;
  }
  .label::before{
    content:"";position:absolute;inset:10px;
    border:1.5px solid var(--frame);border-radius:18px;
  }

  .tube-label{left:90px;top:180px;width:200px;height:420px}
  .tube-label .wordmark{
    position:absolute;left:50%;top:48px;transform:translateX(-50%);
    writing-mode:vertical-rl;
    font-family:"Jost",sans-serif;font-weight:600;font-size:52px;letter-spacing:4px;color:var(--ink);
  }
  .tube-label .product{
    position:absolute;left:0;right:0;top:318px;text-align:center;
    font-family:"Montserrat",sans-serif;font-weight:600;font-size:13px;letter-spacing:5px;color:var(--ink-soft);
  }
  .tube-label .variant{
    position:absolute;left:0;right:0;top:352px;text-align:center;
    font-family:"Jost",sans-serif;font-size:15px;color:var(--ink);
  }

  .jar-label{left:130px;top:80px;width:300px;height:140px}
  .jar-label .wordmark{
    position:absolute;left:0;right:0;top:24px;text-align:center;
    font-family:"Jost",sans-serif;font-weight:600;font-size:36px;letter-spacing:4px;color:var(--ink);line-height:1;
  }
  .jar-label .sub{
    position:absolute;left:0;right:0;top:68px;text-align:center;
    font-family:"Jost",sans-serif;font-size:11px;letter-spacing:14px;color:var(--ink);padding-left:14px;
  }
  .jar-label .product{
    position:absolute;left:0;right:0;top:98px;text-align:center;
    font-family:"Montserrat",sans-serif;font-weight:600;font-size:9px;letter-spacing:4px;color:var(--ink-soft);
  }

  .seal{
    position:absolute;border-radius:50%;
    background:var(--label);border:1.5px solid var(--frame);
  }
  .tube-face .seal{left:250px;top:150px;width:62px;height:62px}
  .jar-wrap .seal{left:105px;top:62px;width:44px;height:44px}
</style>
</head>
<body>
<main class="canvas">
  <section class="tube-face">
    <div class="pattern" role="img" aria-label="Decorative wavy line pattern in pink, teal and light blue blobs"></div>
    <div class="label tube-label">
      <span class="wordmark">valiremo</span>
      <p class="product">BODY CREAM</p>
      <p class="variant">tube 2 example</p>
    </div>
    <div class="seal" aria-label="Cruelty-free seal"></div>
  </section>

  <section class="jar-wrap">
    <div class="pattern" role="img" aria-label="Decorative wavy line pattern in pink, teal and light blue blobs"></div>
    <div class="label jar-label">
      <p class="wordmark">valiremo</p>
      <p class="sub">beauty</p>
      <p class="product">BODY CREAM</p>
    </div>
    <div class="seal" aria-label="Cruelty-free seal"></div>
  </section>
</main>
</body>
</html>
```